Healthcare IT firm needs classy and unique business care design

We need a business card design that incorporates our new logo design (attached) Prefer a purple based designed. I would really love to see something utilizing the "3D" version of the logo (purple on the reflective wall). I want something a little more than my logo printed along with a person's detailed contact information.
Contact Information for Business Card
Want something polished, professional, and a little unique in the design.
Colors
6b449b
Requirements
Must have
- Please use similar font as the logo design
Nice to have
- Would like to see the 3d version of my logo incorporated into the design.

```html
<!DOCTYPE html>
<html lang="en">
<head>
<meta charset="utf-8">
<title>Velora Health Systems – Business Card</title>
<link href="https://fonts.googleapis.com/css2?family=Lato:wght@400;700;900&display=swap" rel="stylesheet">
<style>
  :root {
    --canvas-bg: #2f2b29;
    --card-purple: #6b449b;
    --card-purple-light: #7a54ab;
    --card-purple-deep: #643f93;
    --ink-white: #ffffff;
    --foil-silver: #e2e2e8;
  }
  * { margin: 0; padding: 0; box-sizing: border-box; }
  html, body {
    width: 1200px;
    height: 769px;
    overflow: hidden;
    background: var(--canvas-bg);
  }
  .stage {
    width: 1200px;
    height: 769px;
    display: flex;
    align-items: center;
    justify-content: center;
    gap: 60px;
  }
  .card {
    width: 520px;
    height: 297px;
    border-radius: 3px;
    background: linear-gradient(160deg, var(--card-purple-light) 0%, var(--card-purple) 55%, var(--card-purple-deep) 100%);
    box-shadow: 0 14px 30px rgba(0,0,0,0.5);
    position: relative;
    font-family: "Lato", Arial, sans-serif;
    color: var(--ink-white);
  }
  /* Back: contact details */
  .contact {
    position: absolute;
    left: 0;
    right: 0;
    top: 62px;
    text-align: center;
  }
  .person-name {
    font-size: 19px;
    font-weight: 700;
    letter-spacing: 0.6px;
    text-transform: uppercase;
    line-height: 1.1;
  }
  .person-role {
    font-size: 13px;
    font-weight: 400;
    text-transform: uppercase;
    letter-spacing: 0.3px;
    margin-bottom: 16px;
  }
  .address, .lines {
    font-size: 13.5px;
    line-height: 1.4;
  }
  .address { margin-bottom: 14px; }
  /* Front: foil brand lockup */
  .card-front .brand {
    position: absolute;
    left: 118px;
    top: 96px;
    display: flex;
    align-items: center;
    gap: 16px;
  }
  .brand-square {
    width: 52px;
    height: 52px;
    background: var(--foil-silver);
    flex: none;
  }
  .brand-name {
    font-size: 38px;
    font-weight: 900;
    line-height: 0.95;
    color: var(--foil-silver);
    letter-spacing: -0.3px;
    width: 250px;
  }
</style>
</head>
<body>
  <main class="stage">
    <section class="card card-back" aria-label="Card back with contact details">
      <div class="contact">
        <p class="person-name">Daniel Reyes</p>
        <p class="person-role">CEO/Founder</p>
        <p class="address">2140 Linden Court<br>Fairbanks, Alaska 99701</p>
        <p class="lines">p. 555 218 4096<br>e. hello@velorahs.com<br>w. velorahs.com</p>
      </div>
    </section>
    <section class="card card-front" aria-label="Card front with silver foil company name">
      <div class="brand">
        <span class="brand-square"></span>
        <span class="brand-name">Velora Health Systems</span>
      </div>
    </section>
  </main>
</body>
</html>
```